Real Estate Company Needs a Contemporary/Modern Business Card Design

We need a Contemporary/Modern Business Card Design for a New Real Estate Company based in San Francisco, CA called Tolvash Orrin Realtors. We would like to see designs that use the color red for the "Tolvash Orrin" and gold for the "Realtors." The design should communicate being Modern and yet Established and Stable.
Updates

Project Deadline Extended
Reason: Waiting for more designs and/or revisions.

Industry/Entity Type

Business

```html
<!DOCTYPE html>
<html lang="en">
<head>
<meta charset="utf-8">
<title>Tolvash Orrin Realtors – Business Card</title>
<link rel="stylesheet" href="https://fonts.googleapis.com/css2?family=Saira+Condensed:wght@500&family=Open+Sans:wght@400&display=swap">
<style>
  :root {
    --brand-red: #e30b17;
    --brand-gold: #85744a;
    --ink-grey: #6e6e6e;
    --card-line: #333333;
    --paper: #ffffff;
  }
  html, body {
    margin: 0;
    padding: 0;
    width: 878px;
    height: 1200px;
    overflow: hidden;
    background: var(--paper);
  }
  .sheet {
    position: relative;
    width: 878px;
    height: 1200px;
  }
  .card {
    position: absolute;
    left: 42px;
    width: 798px;
    box-sizing: border-box;
  }
  /* Front */
  .card-front {
    top: 19px;
    height: 522px;
    background: var(--brand-gold);
  }
  .front-panel {
    position: absolute;
    left: 235px;
    top: 15px;
    width: 549px;
    height: 492px;
    background: var(--brand-red);
  }
  .wordmark {
    position: absolute;
    right: 55px;
    text-align: right;
    font-family: "Saira Condensed", "Arial Narrow", sans-serif;
    font-weight: 500;
    text-transform: uppercase;
    line-height: 1;
    white-space: nowrap;
  }
  .wordmark-name,
  .wordmark-tag {
    display: block;
  }
  .card-front .wordmark {
    top: 330px;
    color: var(--paper);
  }
  .card-front .wordmark-name {
    font-size: 64px;
    letter-spacing: 0.6px;
  }
  .card-front .wordmark-tag {
    font-size: 38px;
    margin-top: 2px;
  }
  /* Back */
  .card-back {
    top: 632px;
    height: 521px;
    background: var(--paper);
    border: 1px solid var(--card-line);
  }
  .staff {
    position: absolute;
    left: 64px;
    top: 54px;
    font-family: "Open Sans", Verdana, sans-serif;
    color: var(--ink-grey);
  }
  .staff-name {
    margin: 0;
    font-size: 35px;
    font-weight: 400;
    line-height: 1.1;
    letter-spacing: 0.5px;
  }
  .staff-role {
    margin: 0;
    font-size: 24px;
    line-height: 1.2;
  }
  .contact {
    position: absolute;
    left: 64px;
    top: 193px;
    margin: 0;
    padding: 0;
    list-style: none;
    font-family: "Open Sans", Verdana, sans-serif;
    font-size: 22px;
    line-height: 28.5px;
    color: var(--ink-grey);
  }
  .contact-label {
    display: inline-block;
    width: 48px;
  }
  .card-back .wordmark {
    top: 362px;
  }
  .card-back .wordmark-name {
    font-size: 54px;
    color: var(--brand-red);
  }
  .card-back .wordmark-tag {
    font-size: 33px;
    margin-top: 2px;
    color: var(--brand-gold);
  }
</style>
</head>
<body>
<main class="sheet">
  <section class="card card-front" aria-label="Card front">
    <div class="front-panel">
      <div class="wordmark">
        <span class="wordmark-name">Tolvash Orrin</span>
        <span class="wordmark-tag">Realtors</span>
      </div>
    </div>
  </section>

  <section class="card card-back" aria-label="Card back">
    <div class="staff">
      <h1 class="staff-name">STAFF NAME</h1>
      <p class="staff-role">position</p>
    </div>
    <ul class="contact">
      <li><span class="contact-label">T</span>000.000.000</li>
      <li><span class="contact-label">M</span>000.000.000</li>
      <li>San Francisco, CA</li>
      <li>email1234@email.com</li>
      <li>website.0123456.com</li>
    </ul>
    <div class="wordmark">
      <span class="wordmark-name">Tolvash Orrin</span>
      <span class="wordmark-tag">Realtors</span>
    </div>
  </section>
</main>
</body>
</html>
```